Kelmora Business Card

We want a logo that connects with the target consumer who are Retailers in the giftware/wholesale/ecommerce space. We will be constantly changing product lines and industry. We are after a logo that can communicate the meaning of "Kelmora"which means Divine/spiritual/light. The company name and owners are of Indian nationals and want to bring the positivity/growth in the design as a subtle message.
Have attached a logo that we think captures the essence of the word "Kelmora" which is light/glow/divine.

Target Market(s)

Adults based in Australia english speaking aged 20 - 60 years that are in the retail business.

Industry/Entity Type

Business

Font styles to use
Serif
Sans Serif
Decorative
Script

Requirements
Must have
• Logo in form of "D" or "Kelmora" or "Kelmora Pty Ltd"
Nice to have
• I have attached a sample of letter D used as logo. Its shows the glowing sun which is representative/symbolic presentation of word "Kelmora"

```html
<!DOCTYPE html>
<html lang="en">
<head>
<meta charset="utf-8">
<title>Kelmora Business Card</title>
<link href="https://fonts.googleapis.com/css2?family=Kurale&display=swap" rel="stylesheet">
<style>
  :root {
    --backdrop: #e9e4de;
    --card-dark: #050505;
    --card-light: #ffffff;
    --brand-orange: #ee5a1c;
    --glow-peach: #f9d3b6;
    --ink: #151515;
  }
  * { margin: 0; padding: 0; box-sizing: border-box; }
  html, body { width: 1200px; height: 900px; overflow: hidden; }
  body {
    background: var(--backdrop);
    font-family: "Kurale", Georgia, serif;
    color: var(--ink);
    position: relative;
  }
  .card {
    position: absolute;
    left: 267px;
    width: 666px;
    height: 380px;
    border-radius: 4px;
    box-shadow: 0 10px 28px rgba(0,0,0,0.25);
    overflow: hidden;
  }
  .card-front { top: 50px; background: var(--card-dark); }
  .card-back { top: 470px; background: var(--card-light); }

  .front-brand {
    position: absolute;
    inset: 0;
    display: flex;
    align-items: center;
    justify-content: center;
    gap: 22px;
  }
  .brand-square {
    width: 86px; height: 86px;
    background: var(--brand-orange);
  }
  .brand-name {
    color: var(--brand-orange);
    font-size: 78px;
    line-height: 1;
    font-weight: 400;
  }

  .glow-circle {
    position: absolute;
    right: -40px; top: 20px;
    width: 270px; height: 270px;
    border-radius: 50%;
    background: var(--glow-peach);
  }
  .back-content {
    position: absolute;
    left: 50px; top: 42px;
  }
  .back-brand { font-size: 62px; color: var(--brand-orange); line-height: 1; }
  .holder-name {
    margin-top: 26px;
    font-size: 24px;
    color: var(--brand-orange);
    text-transform: uppercase;
    letter-spacing: 0.5px;
  }
  .holder-role { font-size: 18px; font-weight: 700; margin-top: 2px; }
  .contact-list { list-style: none; margin-top: 30px; }
  .contact-list li {
    display: flex; align-items: center; gap: 12px;
    font-size: 19px; line-height: 30px;
  }
  .contact-icon { width: 18px; height: 18px; flex: none; }
  .address { margin-top: 30px; font-size: 20px; }
</style>
</head>
<body>
  <section class="card card-front" aria-label="Card front">
    <div class="front-brand">
      <div class="brand-square"></div>
      <span class="brand-name">Kelmora</span>
    </div>
  </section>

  <section class="card card-back" aria-label="Card back">
    <div class="glow-circle"></div>
    <div class="back-content">
      <div class="back-brand">Kelmora</div>
      <div class="holder-name">Ravi Mehta</div>
      <div class="holder-role">Manager</div>
      <ul class="contact-list">
        <li>
          <svg class="contact-icon" viewBox="0 0 24 24" aria-hidden="true">
            <path d="M6.6 10.8a15 15 0 0 0 6.6 6.6l2.2-2.2a1 1 0 0 1 1-.25 11.4 11.4 0 0 0 3.6.57 1 1 0 0 1 1 1V20a1 1 0 0 1-1 1A17 17 0 0 1 3 4a1 1 0 0 1 1-1h3.5a1 1 0 0 1 1 1c0 1.25.2 2.45.57 3.57a1 1 0 0 1-.25 1z" fill="#ee5a1c"/>
          </svg>
          +61 400 555 018
        </li>
        <li>
          <svg class="contact-icon" viewBox="0 0 24 24" aria-hidden="true">
            <rect x="2" y="5" width="20" height="14" fill="#ee5a1c"/>
            <path d="M2 5l10 8 10-8" fill="none" stroke="#fff" stroke-width="1.6"/>
          </svg>
          ravi@kelmora.com
        </li>
        <li>
          <svg class="contact-icon" viewBox="0 0 24 24" aria-hidden="true">
            <rect x="2.5" y="4" width="19" height="12" fill="none" stroke="#ee5a1c" stroke-width="2"/>
            <path d="M9 20h6M12 16v4" stroke="#ee5a1c" stroke-width="2"/>
          </svg>
          www.kelmora.com
        </li>
      </ul>
      <div class="address">Building No., Street No., City State Zip</div>
    </div>
  </section>
</body>
</html>
```